RTV CRAFTED

building services
decks
pergola
renovation
extensions
general building

Target Market(s)

middle to upper class

Industry/Entity Type

building

Contact Information for Business Card

my details 0427839152 pkharlow47@mailvane.net BLD574926

Font styles to use
Serif

Colors
00AB8E
00BBA5
67D7C9
C6EFE9
E9F9F6

Requirements
Must have
• logo on the front and details on the back
Nice to have
• sharp and clean lines

```html
<!DOCTYPE html>
<html lang="en">
<head>
<meta charset="utf-8">
<title>RTV Crafted – Business Cards</title>
<link rel="stylesheet" href="https://fonts.googleapis.com/css2?family=Lora:wght@400;700&family=Roboto:wght@400;500&display=swap">
<style>
  :root {
    --page-bg: #1b1b1c;
    --card-dark: #2d2d2f;
    --teal: #00ab8e;
    --teal-bright: #00bba5;
    --white: #ffffff;
    --ink: #2a2a2a;
  }
  * { margin: 0; padding: 0; box-sizing: border-box; }
  html, body { width: 1200px; height: 1015px; overflow: hidden; background: var(--page-bg); }
  .sheet {
    width: 1200px; height: 1015px;
    display: flex; flex-direction: column; align-items: center; justify-content: center; gap: 15px;
  }
  .card {
    width: 840px; height: 480px; position: relative; overflow: hidden;
    background: var(--card-dark); color: var(--white);
  }
  .wordmark {
    position: absolute; display: flex; align-items: center; gap: 14px;
    font-family: "Lora", serif; font-weight: 400; letter-spacing: 4px; color: var(--white);
  }
  .wordmark-square { width: 14px; height: 14px; background: var(--teal); }
  .wordmark-rule { position: absolute; height: 5px; background: var(--teal); }

  /* front */
  .card-front .wordmark { left: 70px; top: 70px; font-size: 54px; }
  .card-front .wordmark-rule { left: 70px; top: 142px; width: 400px; }
  .services {
    position: absolute; left: 70px; top: 200px; list-style: none;
    font-family: "Roboto", sans-serif; font-size: 20px; letter-spacing: 1.5px; line-height: 34px;
  }
  .services li { display: flex; align-items: center; gap: 14px; }
  .services li::before { content: ""; width: 11px; height: 11px; background: var(--teal); }

  /* back */
  .card-back .wordmark { left: 0; right: 0; justify-content: center; top: 90px; font-size: 58px; }
  .card-back .wordmark-rule { left: 240px; top: 168px; width: 380px; }
  .band-teal {
    position: absolute; left: 0; top: 232px; width: 100%; height: 138px; background: var(--teal);
    display: flex; align-items: center; justify-content: center; gap: 40px;
  }
  .person { text-align: right; }
  .person-name { font-family: "Lora", serif; font-weight: 700; font-size: 32px; letter-spacing: 1px; }
  .person-role { font-family: "Roboto", sans-serif; font-size: 22px; letter-spacing: 1px; }
  .divider { width: 2px; height: 80px; background: var(--white); }
  .contacts { font-family: "Roboto", sans-serif; font-size: 22px; letter-spacing: 1px; line-height: 36px; }
  .contact { display: flex; align-items: center; gap: 12px; }
  .contact svg { width: 22px; height: 22px; }
  .band-white {
    position: absolute; left: 0; top: 370px; width: 100%; height: 90px; background: var(--white);
    display: flex; align-items: center; justify-content: center;
    font-family: "Roboto", sans-serif; font-size: 24px; letter-spacing: 1px; color: var(--ink);
  }
  .licence-prefix { color: var(--teal); }
  .base-strip { position: absolute; left: 0; bottom: 0; width: 100%; height: 20px; }
</style>
</head>
<body>
<main class="sheet">
  <section class="card card-front" aria-label="Card front">
    <div class="wordmark">RTV CRAFTED <span class="wordmark-square"></span></div>
    <div class="wordmark-rule"></div>
    <ul class="services">
      <li>BUILDING SERVICES</li>
      <li>DECKS</li>
      <li>PERGOLA</li>
      <li>RENOVATION</li>
      <li>EXTENSIONS</li>
      <li>GENERAL BUILDING</li>
    </ul>
  </section>

  <section class="card card-back" aria-label="Card back">
    <div class="wordmark">RTV CRAFTED <span class="wordmark-square"></span></div>
    <div class="wordmark-rule"></div>
    <div class="band-teal">
      <div class="person">
        <div class="person-name">MARCUS HALE</div>
        <div class="person-role">Managing Director</div>
      </div>
      <div class="divider"></div>
      <div class="contacts">
        <div class="contact">
          <svg viewBox="0 0 24 24" aria-hidden="true"><path fill="#fff" d="M6.6 10.8a15 15 0 0 0 6.6 6.6l2.2-2.2c.3-.3.7-.4 1-.2 1.1.4 2.3.6 3.6.6.6 0 1 .4 1 1V20c0 .6-.4 1-1 1A17 17 0 0 1 3 4c0-.6.4-1 1-1h3.5c.6 0 1 .4 1 1 0 1.3.2 2.5.6 3.6.1.3 0 .7-.2 1z"/></svg>
          <span>0427839152</span>
        </div>
        <div class="contact">
          <svg viewBox="0 0 24 24" aria-hidden="true"><rect x="2" y="5" width="20" height="14" fill="none" stroke="#fff" stroke-width="2"/><path d="M2 5l10 8 10-8" fill="none" stroke="#fff" stroke-width="2"/></svg>
          <span>pkharlow47@mailvane.net</span>
        </div>
      </div>
    </div>
    <div class="band-white"><span class="licence-prefix">BLD</span>574926</div>
    <svg class="base-strip" viewBox="0 0 840 20" preserveAspectRatio="none" aria-hidden="true">
      <polygon points="0,0 560,0 550,20 0,20" fill="#2d2d2f"/>
      <polygon points="568,0 840,0 840,20 558,20" fill="#00ab8e"/>
    </svg>
  </section>
</main>
</body>
</html>
```